Wine label refresh

We are wanting to modify our Corran Estate label to include a picture on it.
I have attached the pictures below which we would like on the label. They are of the Corran Estate vineyard. I have also attached an example of another label with a picture on it that we like the style of.
Industry/Entity Type
Vineyard
Requirements
Must have
- The Corran Estate text must stay the same but can be moved down. It still needs to be the same size though.
Marlborough Sauvignon Blanc should remain in the same font and roughly the same size.
Wine of New Zealand also must stay but could potentially be moved.
Nice to have
- It would be nice if we could keep the KL logo on the front label but feel free to experiment with where this goes.

```html
<!DOCTYPE html>
<html lang="en">
<head>
<meta charset="utf-8">
<title>Corran Estate – Marlborough Sauvignon Blanc 2012 Label</title>
<link rel="stylesheet" href="https://fonts.googleapis.com/css2?family=Cormorant+Garamond:wght@500&family=Pinyon+Script&family=Lato:wght@300&display=swap">
<style>
  :root {
    --page: #ffffff;
    --trim-blue: #29abe2;
    --keyline: #222222;
    --gold: #d9961a;
    --label-white: #ffffff;
    --text-white: #ffffff;
    --text-soft: rgba(255, 255, 255, 0.62);
    --sky: #c9cbcd;
    --hills: #7f9a6a;
    --vines: #5f8a3a;
    --grass: #6f9a45;
  }
  * { margin: 0; padding: 0; box-sizing: border-box; }
  html, body {
    width: 1200px; height: 899px; overflow: hidden;
    background: var(--page);
  }
  .canvas { position: relative; width: 1200px; height: 899px; }
  .trim-line {
    position: absolute; left: 10px; top: 10px; width: 1177px; height: 880px;
    border: 2px solid var(--trim-blue); border-radius: 8px;
  }
  .keyline {
    position: absolute; left: 34px; top: 42px; width: 1129px; height: 821px;
    border: 1.5px solid var(--keyline);
  }
  .gold-band {
    position: absolute; left: 59px; top: 67px; width: 1079px; height: 771px;
    background: var(--gold);
  }
  .white-mat {
    position: absolute; left: 92px; top: 100px; width: 1013px; height: 704px;
    background: var(--label-white);
  }
  .gold-rule {
    position: absolute; left: 102px; top: 110px; width: 993px; height: 684px;
    border: 2px solid var(--gold);
  }
  .vineyard-photo {
    position: absolute; left: 106px; top: 114px; width: 986px; height: 677px;
    background: linear-gradient(180deg,
      var(--sky) 0%, #b9bcbe 30%, var(--hills) 40%,
      var(--vines) 52%, var(--grass) 75%, #8a8a5c 100%);
    overflow: hidden;
  }
  .brand-mark {
    position: absolute; left: 0; width: 100%; top: 86px;
    text-align: center; padding-left: 72px;
    font-family: "Cormorant Garamond", serif; font-weight: 500;
    font-size: 110px; line-height: 1; letter-spacing: 4px;
    color: var(--gold);
  }
  .estate-name {
    position: absolute; left: 0; width: 100%; top: 281px;
    text-align: center;
    font-family: "Cormorant Garamond", serif; font-weight: 500;
    font-size: 88px; line-height: 1; letter-spacing: 4px;
    font-variant: small-caps; color: var(--text-white);
  }
  .varietal {
    position: absolute; left: 0; width: 100%; top: 398px;
    text-align: center; padding-right: 20px;
    font-family: "Pinyon Script", cursive; font-size: 74px; line-height: 1;
    color: var(--text-white);
  }
  .vintage {
    position: absolute; left: 0; width: 100%; top: 483px;
    text-align: center; padding-right: 20px;
    font-family: "Pinyon Script", cursive; font-size: 58px; line-height: 1;
    color: var(--text-white);
  }
  .label-footer {
    position: absolute; left: 0; width: 100%; top: 611px; height: 50px;
    font-family: "Lato", sans-serif; font-weight: 300;
    font-size: 40px; line-height: 1; color: var(--text-soft);
  }
  .volume { position: absolute; left: 12px; top: 0; }
  .origin { position: absolute; left: 0; width: 100%; top: 0; text-align: center; padding-right: 28px; }
  .alcohol { position: absolute; right: 34px; top: 0; }
</style>
</head>
<body>
<div class="canvas">
  <div class="trim-line"></div>
  <div class="keyline"></div>
  <div class="gold-band"></div>
  <div class="white-mat"></div>
  <div class="gold-rule"></div>
  <div class="vineyard-photo" role="img" aria-label="Photograph of the Corran Estate vineyard: rows of vines on green grass, palm trees and a farmhouse beneath grey cloudy sky and rolling hills">
    <div class="brand-mark">KL</div>
    <div class="estate-name">Corran Estate</div>
    <div class="varietal">Marlborough Sauvignon Blanc</div>
    <div class="vintage">2012</div>
    <div class="label-footer">
      <span class="volume">750ml</span>
      <span class="origin">NEW ZEALAND WINE</span>
      <span class="alcohol">13% alc/vol</span>
    </div>
  </div>
</div>
</body>
</html>
```